Double-sided business card needed - specific brief

We need a double sided business card designed for our company Radiant Trimline. Having lost a lot of weight myself, the back of the card needs to show my before and after pictures. It needs to cover the entire back side of the card. This might be with my two before pictures over set on top of my main after picture or in separate frames. I'll leave that to your artistic consideration. The front needs to have our logo with contact details centred below.

The cards will be printed by PRINTKO.com and will be rectangular, 84mm x 55mm, but with ROUNDED edges. Please therefore present your designs rectangular but with rounded edges if possible.

The card should be designed in LANDSCAPE orientation.

As well as the logo, the front of the card should have the following details:

Moira Blakewell
Weight Loss Motivator with 189lb personal loss
moira@radiant-trimline.example
+44 (0)7700 900418

The website is important so should perhaps be more bold than the rest:
www.radiant-trimline.example

My brand colours are: Pink #CD2366, Light Pink #FD88AD. Blue #1C9CB1, Light Blue #64C4DE

Target Market(s)

Women 30+

Contact Information for Business Card

As description above

Font styles to use
Sans Serif

Requirements
Must have
• Double sided.
• Back side entirely covered with my before and after pictures.
• You may wish to float my before pictures on top of my after picture or add them in different frames. I look forward to seeing your different suggestions.

```html
<!DOCTYPE html>
<html lang="en">
<head>
<meta charset="utf-8">
<title>Radiant Trimline – Business Card</title>
<link href="https://fonts.googleapis.com/css2?family=Arimo:wght@400;700&display=swap" rel="stylesheet">
<style>
  :root {
    --pink: #CD2366;
    --light-pink: #FD88AD;
    --blue: #1C9CB1;
    --light-blue: #64C4DE;
    --card-white: #f7f7f7;
    --backdrop: #2b2b2b;
    --text-dark: #2a2a2a;
  }
  * { margin: 0; padding: 0; box-sizing: border-box; }
  html, body {
    width: 1200px; height: 997px; overflow: hidden;
    background: var(--backdrop);
    font-family: "Arimo", Arial, sans-serif;
  }
  .stage {
    position: relative; width: 1200px; height: 997px;
    display: flex; flex-direction: column; align-items: center; justify-content: center; gap: 44px;
  }
  .card {
    position: relative; width: 640px; height: 419px;
    border-radius: 26px; overflow: hidden; background: var(--card-white);
  }
  .card svg.card-art { position: absolute; inset: 0; width: 100%; height: 100%; }

  /* front */
  .brand {
    position: absolute; top: 112px; left: 0; width: 100%;
    text-align: center; color: var(--pink);
    font-size: 40px; font-weight: 400; letter-spacing: 2px; text-transform: uppercase;
  }
  .holder { position: absolute; left: 90px; top: 318px; }
  .holder-name { color: var(--pink); font-size: 21px; text-transform: uppercase; letter-spacing: .5px; }
  .holder-role { color: #fff; font-size: 16px; margin-top: 4px; }
  .divider { position: absolute; left: 340px; top: 262px; width: 1px; height: 110px; background: rgba(255,255,255,.7); }
  .contacts { position: absolute; left: 358px; top: 262px; list-style: none; }
  .contacts li { display: flex; align-items: center; gap: 9px; height: 32px; font-size: 13.5px; color: var(--text-dark); white-space: nowrap; }
  .contacts li.web { color: var(--pink); font-weight: 700; font-size: 14px; }
  .contacts .icon { width: 18px; height: 18px; flex: none; }

  /* back */
  .photo-label { font-family: "Arimo", Arial, sans-serif; font-size: 14px; }
</style>
</head>
<body>
<main class="stage">

  <section class="card card-back" aria-label="Card back">
    <svg class="card-art" viewBox="0 0 640 419" xmlns="http://www.w3.org/2000/svg">
      <defs>
        <linearGradient id="before-main" x1="0" y1="0" x2="1" y2="1">
          <stop offset="0" stop-color="#8a7a62"/><stop offset="1" stop-color="#d9d6d2"/>
        </linearGradient>
        <linearGradient id="after-main" x1="0" y1="0" x2="1" y2="1">
          <stop offset="0" stop-color="#c9ccc6"/><stop offset="1" stop-color="#e8dccb"/>
        </linearGradient>
        <linearGradient id="before-small" x1="0" y1="0" x2="0" y2="1">
          <stop offset="0" stop-color="#d9c7a8"/><stop offset="1" stop-color="#8a5a4a"/>
        </linearGradient>
        <linearGradient id="after-small" x1="0" y1="0" x2="0" y2="1">
          <stop offset="0" stop-color="#c9b9a0"/><stop offset="1" stop-color="#e07a45"/>
        </linearGradient>
      </defs>
      <rect width="640" height="419" fill="var(--card-white)"/>
      <circle cx="165" cy="262" r="172" fill="url(#before-main)" role="img" aria-label="Before photo: owner in a white shirt, outdoors"/>
      <circle cx="165" cy="262" r="172" fill="none" stroke="var(--blue)" stroke-width="12"/>
      <circle cx="478" cy="168" r="172" fill="url(#after-main)" role="img" aria-label="After photo: owner in a white top, standing"/>
      <circle cx="478" cy="168" r="172" fill="none" stroke="var(--blue)" stroke-width="12"/>
      <circle cx="292" cy="88" r="52" fill="url(#before-small)" stroke="var(--pink)" stroke-width="7" role="img" aria-label="Before close-up photo"/>
      <circle cx="305" cy="338" r="56" fill="url(#after-small)" stroke="var(--pink)" stroke-width="7" role="img" aria-label="After photo in an orange top"/>
      <text class="photo-label" x="280" y="124" fill="var(--pink)" transform="rotate(-25 280 124)">Before</text>
      <text class="photo-label" x="190" y="398" fill="var(--pink)" transform="rotate(-25 190 398)">Before</text>
      <text class="photo-label" x="486" y="290" fill="var(--blue)" transform="rotate(-25 486 290)">After</text>
    </svg>
  </section>

  <section class="card card-front" aria-label="Card front">
    <svg class="card-art" viewBox="0 0 640 419" xmlns="http://www.w3.org/2000/svg" aria-hidden="true">
      <rect width="640" height="419" fill="var(--card-white)"/>
      <path d="M0 330 C150 230 360 205 640 215 L640 419 L0 419 Z" fill="var(--blue)"/>
      <path d="M40 330 C190 235 400 200 620 208 C400 212 200 250 40 330 Z" fill="var(--pink)"/>
    </svg>

    <div class="brand">Radiant Trimline</div>

    <div class="holder">
      <p class="holder-name">Moira Blakewell</p>
      <p class="holder-role">Weight Loss Motivator</p>
    </div>

    <div class="divider"></div>

    <ul class="contacts">
      <li>
        <svg class="icon" viewBox="0 0 18 18"><circle cx="9" cy="9" r="9" fill="#fff"/><path d="M5.5 7.5h7v4h-7z M6.5 7.5a2.5 2 0 0 1 5 0" fill="none" stroke="var(--blue)" stroke-width="1.4"/></svg>
        +44 (0)7700 900418
      </li>
      <li>
        <svg class="icon" viewBox="0 0 18 18"><circle cx="9" cy="9" r="9" fill="#fff"/><rect x="5" y="6" width="8" height="6" fill="none" stroke="var(--blue)" stroke-width="1.4"/><path d="M5 6l4 3 4-3" fill="none" stroke="var(--blue)" stroke-width="1.2"/></svg>
        moira@radiant-trimline.example
      </li>
      <li class="web">
        <svg class="icon" viewBox="0 0 18 18"><circle cx="9" cy="9" r="9" fill="#fff"/><circle cx="9" cy="9" r="4" fill="none" stroke="var(--blue)" stroke-width="1.4"/><path d="M5 9h8" stroke="var(--blue)" stroke-width="1.2"/></svg>
        www.radiant-trimline.example
      </li>
    </ul>
  </section>

</main>
</body>
</html>
```